business card for LWR pty ltd

We require a business card that stands out . I have included our company flyer and would like the services listed to be put on the card so when we Give out the cards to customers they have an idea of services we provide. need the winning design to be in editable photo shop format, editable iMac pages format or editable windows publisher format, so that I can enter in names, email addresses, phone numbers etc myself. I have included a pdf documents of info / items needed on the card to use as reference please.
Updates

need more submissions

Need extra days to review

Sick

Target Market(s)

new customers

Contact Information for Business Card

details are on attached business card requirements file

Requirements
Must have
• I have attached a list of must haves

```html
<!DOCTYPE html>
<html lang="en">
<head>
<meta charset="utf-8">
<title>LWR pty ltd – Business Card</title>
<link href="https://fonts.googleapis.com/css2?family=Roboto:wght@400;500;700;900&display=swap" rel="stylesheet">
<style>
  :root {
    --page-bg: #3a3a3a;
    --card-black: #050505;
    --mesh-light: #3b3b3b;
    --mesh-dark: #0a0a0a;
    --silver-light: #d9d9d9;
    --silver-mid: #9a9a9a;
    --silver-dark: #5e5e5e;
    --text-light: #f2f2f2;
    --text-muted: #bdbdbd;
    --desert: #b8875a;
    --desert-dark: #6b4a2e;
  }
  * { margin: 0; padding: 0; box-sizing: border-box; }
  html, body { width: 1200px; height: 976px; overflow: hidden; }
  body {
    background: var(--page-bg);
    font-family: "Roboto", Arial, sans-serif;
    display: flex;
    flex-direction: column;
    align-items: center;
    justify-content: center;
    gap: 30px;
  }
  .card {
    position: relative;
    width: 760px;
    height: 434px;
    background: var(--card-black);
    overflow: hidden;
    box-shadow: 0 12px 30px rgba(0,0,0,.55);
  }
  .mesh {
    position: absolute;
    background: radial-gradient(ellipse at 50% 40%, var(--mesh-light) 0%, #1c1c1c 45%, var(--mesh-dark) 80%);
  }
  .brand-name {
    position: absolute;
    font-weight: 900;
    color: var(--silver-light);
    letter-spacing: 4px;
    line-height: 1;
  }

  /* Front */
  .card-front .mesh { left: 120px; top: 0; width: 430px; height: 434px; }
  .card-front .brand-name { left: 200px; top: 80px; font-size: 120px; }
  .fleet-photo {
    position: absolute;
    left: 215px; top: 170px;
    width: 545px; height: 264px;
    background: linear-gradient(160deg, #1a1a1a 0%, #2a2420 30%, var(--desert-dark) 55%, var(--desert) 85%, #c99a6c 100%);
    clip-path: polygon(0 30%, 100% 0, 100% 100%, 0 100%);
  }

  /* Back */
  .card-back .mesh { left: 0; top: 0; width: 470px; height: 320px; clip-path: polygon(0 0, 100% 0, 85% 100%, 0 100%); }
  .card-back .brand-name { left: 95px; top: 120px; font-size: 110px; }
  .contact {
    position: absolute;
    left: 455px; top: 55px;
    color: var(--text-light);
  }
  .contact .person { font-size: 27px; font-weight: 700; letter-spacing: 1px; color: var(--silver-light); }
  .contact .role { font-size: 16px; color: var(--text-muted); margin-bottom: 10px; }
  .contact .company { font-size: 20px; font-weight: 700; }
  .contact .address { font-size: 15px; margin-bottom: 10px; }
  .contact .line { display: flex; align-items: center; gap: 8px; font-size: 15px; margin-top: 4px; }
  .contact svg { width: 13px; height: 13px; fill: var(--text-muted); }
  .services-band {
    position: absolute;
    left: 0; bottom: 0;
    width: 100%; height: 128px;
    background: linear-gradient(90deg, var(--silver-dark) 0%, var(--silver-mid) 40%, var(--silver-light) 70%, var(--silver-mid) 100%);
    border-top: 2px solid #e8e8e8;
    display: flex;
    flex-direction: column;
    justify-content: center;
    padding: 0 28px;
  }
  .services-band p {
    color: #fff;
    font-size: 17px;
    line-height: 1.45;
    text-shadow: 0 1px 2px rgba(0,0,0,.45);
  }
</style>
</head>
<body>
  <section class="card card-front">
    <div class="mesh"></div>
    <div class="fleet-photo" role="img" aria-label="Photograph of a road train truck with tipper trailers on red desert ground"></div>
    <div class="brand-name">LWR</div>
  </section>

  <section class="card card-back">
    <div class="mesh"></div>
    <div class="brand-name">LWR</div>
    <div class="contact">
      <div class="person">DANIEL KORVER</div>
      <div class="role">Director</div>
      <div class="company">LWR pty ltd</div>
      <div class="address">Lot 12 Sample Road Australia</div>
      <div class="line"><svg viewBox="0 0 24 24"><path d="M6.6 10.8a15 15 0 0 0 6.6 6.6l2.2-2.2c.3-.3.7-.4 1-.2 1.1.4 2.3.6 3.6.6.6 0 1 .4 1 1V20c0 .6-.4 1-1 1A17 17 0 0 1 3 4c0-.6.4-1 1-1h3.5c.6 0 1 .4 1 1 0 1.3.2 2.5.6 3.6.1.3 0 .7-.2 1z"/></svg>000 555 000</div>
      <div class="line"><svg viewBox="0 0 24 24"><path d="M2 5h20v14H2zm2 2v.5l8 5 8-5V7zm0 2.9V17h16V9.9l-8 5z"/></svg>info@lwrservices.com.au</div>
      <div class="line"><svg viewBox="0 0 24 24"><path d="M12 2a10 10 0 1 0 0 20 10 10 0 0 0 0-20zm0 2c.9 0 2.1 1.8 2.6 5H9.4C9.9 5.8 11.1 4 12 4zM4.3 11h3a20 20 0 0 0 0 2h-3a8 8 0 0 1 0-2zm5.1 0h5.2a18 18 0 0 1 0 2H9.4a18 18 0 0 1 0-2zm7.3 0h3a8 8 0 0 1 0 2h-3a20 20 0 0 0 0-2zM12 20c-.9 0-2.1-1.8-2.6-5h5.2c-.5 3.2-1.7 5-2.6 5z"/></svg>www.lwrsite.com</div>
    </div>
    <div class="services-band">
      <p>• Over size loads / Hot Shot Loads • Heavy Vehicle Recovery services • Potable Water</p>
      <p>Deliveries • Road Building / Maintenance • Earthworks • Sand &amp; Metal Supply &amp; Cartage</p>
      <p>• Road Train Tippers • Road Train Tankers • Road Train Flat Tops • Drop Deck Trailers</p>
      <p>• Mine site accredited • Equipment &amp; Operators</p>
    </div>
  </section>
</body>
</html>
```